Business Card Design

RETAIL HIGH END CONTEMPORARY WOMEN'S CLOTHING STORE
MODERN, SIMPLE, CLEAN, COOL

WE ARE ALL ABOUT NY and CALIF STYLE.... CLASSY but EDGY..
COOLEST DENIM , Trendsetting, NEUTRAL Pallettes,
Collections : Fig and Stone, Dorian Vesk, PMW, K47, QTB
Don't need names of collections on card. thats just good info
for designer of card.

WOULD LIKE THE FONT TO BE INTERESTING, but CLEAN
We are on facebook daily with photos of outfits we put together
which you can look up and friend us.... MolvaHarbor
Also on instagram .
Open to options on color and size, but need cool and fresh.

Contact Information for Business Card

DELLA 5417 Larkmoor Rd. #309 Ember Court Arcade..Va. Beach, Va. 23987
Phone 757.386.5049 Fax 757.386-2613 EMAIL..DELLAMODE@QUILLBOX.COM

```html
<!DOCTYPE html>
<html lang="en">
<head>
<meta charset="utf-8">
<title>DELLA — Business Card</title>
<link href="https://fonts.googleapis.com/css2?family=Ubuntu+Condensed&display=swap" rel="stylesheet">
<style>
  :root {
    --frame: #c272b5;
    --card: #8fc4d6;
    --ornament: #7fb6ca;
    --ink: #111214;
    --icon-fill: #f2f6f8;
  }
  html, body {
    margin: 0;
    padding: 0;
    width: 1200px;
    height: 692px;
    overflow: hidden;
    background: #ffffff;
  }
  .card {
    position: relative;
    width: 1200px;
    height: 692px;
    box-sizing: border-box;
    background: var(--frame);
    padding: 11px;
    font-family: "Ubuntu Condensed", "Arial Narrow", sans-serif;
    color: var(--ink);
  }
  .card-face {
    position: relative;
    width: 100%;
    height: 100%;
    background: var(--card);
    overflow: hidden;
  }
  .card-face p, .card-face h1, .card-face address { white-space: nowrap; }
  .backdrop-pattern {
    position: absolute;
    inset: 0;
    background:
      radial-gradient(circle at 30% 35%, var(--ornament) 0, rgba(127,182,202,0.6) 22%, rgba(143,196,214,0) 42%),
      radial-gradient(circle at 85% 80%, rgba(127,182,202,0.55) 0, rgba(143,196,214,0) 30%);
  }
  .brand-name {
    position: absolute;
    left: 30px;
    top: 4px;
    margin: 0;
    font-size: 190px;
    line-height: 1;
    font-weight: 400;
    letter-spacing: 1px;
  }
  .address {
    position: absolute;
    left: 711px;
    top: 38px;
    margin: 0;
    font-style: normal;
    font-size: 36px;
    line-height: 70px;
  }
  .contact-line {
    position: absolute;
    display: flex;
    align-items: center;
    margin: 0;
  }
  .contact-line svg { flex: none; }
  .phone-line  { left: 711px; top: 262px; }
  .fax-line    { left: 711px; top: 372px; }
  .social-line { left: 52px;  top: 395px; }
  .email-line  { left: 52px;  top: 549px; }
  .number {
    font-size: 56px;
    margin-left: 14px;
    line-height: 1;
  }
  .social-mark {
    width: 77px;
    height: 113px;
    background: var(--ink);
  }
  .social-handle {
    font-size: 68px;
    margin-left: 30px;
    line-height: 1;
  }
  .email {
    font-size: 38px;
    margin-left: 24px;
    line-height: 1;
  }
</style>
</head>
<body>
  <div class="card">
    <div class="card-face">
      <div class="backdrop-pattern" role="img" aria-label="Faint circular ornament pattern in soft blue tones"></div>

      <h1 class="brand-name">DELLA</h1>

      <address class="address">
        5417 Larkmoor Rd. #309<br>
        Ember Court Arcade<br>
        Va. Beach, Va. 23987
      </address>

      <p class="contact-line phone-line">
        <svg width="95" height="81" viewBox="0 0 92 80" aria-label="Phone">
          <rect x="0" y="0" width="92" height="80" rx="16" fill="var(--ink)"/>
          <path d="M33 18c3-2 6-1 7 2l4 9c1 2 0 4-2 5l-4 3c3 7 8 12 15 15l3-4c1-2 3-3 5-2l9 4c3 1 4 4 2 7l-3 5c-2 3-6 4-10 3-17-5-29-17-33-34-1-4 0-8 3-10z" fill="var(--icon-fill)"/>
        </svg>
        <span class="number">757.386.5049</span>
      </p>

      <p class="contact-line fax-line">
        <svg width="95" height="76" viewBox="0 0 94 76" aria-label="Fax">
          <rect x="20" y="2" width="54" height="22" fill="none" stroke="var(--ink)" stroke-width="4"/>
          <rect x="3" y="22" width="88" height="52" fill="none" stroke="var(--ink)" stroke-width="5"/>
          <text x="47" y="60" text-anchor="middle" font-family="Ubuntu Condensed, sans-serif" font-size="28" fill="var(--ink)">FAX</text>
        </svg>
        <span class="number">757.386-2613</span>
      </p>

      <p class="contact-line social-line">
        <span class="social-mark" aria-hidden="true"></span>
        <span class="social-handle">MolvaHarbor</span>
      </p>

      <p class="contact-line email-line">
        <svg width="86" height="66" viewBox="0 0 86 66" aria-label="Email">
          <rect x="3" y="3" width="80" height="60" fill="none" stroke="var(--ink)" stroke-width="5"/>
          <path d="M3 3 L43 38 L83 3 M3 63 L33 30 M83 63 L53 30" fill="none" stroke="var(--ink)" stroke-width="5"/>
        </svg>
        <span class="email">DELLAMODE@QUILLBOX.COM</span>
      </p>
    </div>
  </div>
</body>
</html>
```